Wendale Information Posters for Student signage

Secondary school looking for some posters to display throughout the school with fresh designs using school colours and fitting with general feel of the school's graphic image. The final designs should be welcoming but clearly outline the required instructions. Sample designs that have been created by the school are attached with the relevant information that is required to appear on the signs. School would like a more dynamic design than the basic signs attached.
We are looking for:
- Large pop-up banner style size for the 2 posters called
"Ready for class" and "Morning Routine".
- Printable poster for the "Wendale Outdoor" sign.

Please incorporate a design feature of "the Wendale 1,2,3" into the posters and also use the Wendale Leaner values of Integrity, Compassion, Curiosity and Drive to help illustrate the content.

An option for design is to incorporate our school's first nations artwork into the design and i have also provided various extracts of design pieces that the school often uses in it's marketing materials.

Target Market(s)

Secondary School Students

Industry/Entity Type

Education

Colors
00AB8E
00BBA5
67D7C9
C6EFE9
E9F9F6
FFF300
FFF600
FEFA6F
FFFEC7
FFFEE8
FFC000
F8CF3A
FAE287
FDF2CF
FEFAEE

Requirements
Must have
• My project must have eyecatching graphics

```html
<!DOCTYPE html>
<html lang="en">
<head>
<meta charset="utf-8">
<title>Ready for Class – Wendale 1,2,3</title>
<link href="https://fonts.googleapis.com/css2?family=Anton&family=Archivo+Black&display=swap" rel="stylesheet">
<style>
  :root{
    --green-deep:#0b2a17;
    --green-dark:#123d22;
    --green-mid:#1f5a31;
    --teal:#5ccfbe;
    --teal-soft:#67D7C9;
    --yellow:#FFF300;
    --yellow-warm:#F8CF3A;
    --card:#f7f7f2;
    --white:#ffffff;
  }
  *{margin:0;padding:0;box-sizing:border-box}
  html,body{width:848px;height:1200px;overflow:hidden;background:var(--green-deep)}
  .poster{position:relative;width:848px;height:1200px;overflow:hidden;
    font-family:"Anton",sans-serif;color:var(--white)}
  .artwork-bg{position:absolute;inset:0;
    background:radial-gradient(ellipse at 50% 45%,var(--green-mid) 0%,var(--green-dark) 55%,var(--green-deep) 100%)}
  .headline{position:absolute;left:46px;top:52px;line-height:.98;text-transform:uppercase}
  .headline .l1{font-size:92px;letter-spacing:1px}
  .headline .l2{font-size:76px;letter-spacing:1px}
  .headline .l3{font-size:108px;color:var(--yellow);letter-spacing:1px}
  .emblem-art{position:absolute;left:436px;top:58px;width:126px;height:138px;border-radius:50%;
    background:radial-gradient(circle,#3f8a4f 0%,#2a6a3a 50%,rgba(248,207,58,.55) 72%,transparent 74%)}
  .badge{position:absolute;left:460px;top:178px;width:362px;height:158px;
    background:var(--yellow);border-radius:22px;transform:rotate(-3deg);
    box-shadow:0 4px 10px rgba(0,0,0,.35)}
  .badge-top{position:absolute;left:8px;top:10px;right:8px;height:74px;background:var(--green-dark);
    border-radius:14px;display:flex;align-items:center;padding-left:16px;gap:8px}
  .badge-top .the{font-size:24px;color:var(--white)}
  .badge-top .name{font-size:62px;color:var(--yellow);line-height:1}
  .badge-nums{position:absolute;left:0;right:0;top:92px;display:flex;justify-content:center;align-items:flex-end;gap:14px}
  .badge-nums .n{width:56px;height:56px;border-radius:50%;background:var(--green-dark);color:var(--white);
    display:flex;align-items:center;justify-content:center;font-size:38px;border:3px solid var(--white)}
  .badge-nums .comma{color:var(--green-dark);font-size:34px;line-height:1}
  .steps{position:absolute;left:0;top:0;width:848px}
  .step{position:absolute;left:128px;width:648px;background:var(--card);border:5px solid var(--yellow);
    border-radius:28px;box-shadow:0 4px 10px rgba(0,0,0,.3)}
  .step-num{position:absolute;width:90px;height:90px;border-radius:50%;background:var(--green-dark);
    border:6px solid var(--yellow);color:var(--white);font-size:58px;display:flex;align-items:center;justify-content:center}
  .step-icon{position:absolute;width:130px;height:130px;border-radius:50%;background:var(--teal);
    display:flex;align-items:center;justify-content:center}
  .step-label{position:absolute;left:368px;font-family:"Archivo Black",sans-serif;color:var(--green-deep);
    font-size:44px;line-height:1.1;text-transform:uppercase;transform:scaleX(.86);transform-origin:left center}
  .step-label.small{font-size:38px}
  .waves{position:absolute;left:0;top:890px;width:848px;height:160px;
    background:linear-gradient(180deg,transparent 0%,rgba(255,255,255,.12) 45%,transparent 100%)}
  .values{position:absolute;left:66px;top:1020px;text-transform:uppercase;line-height:1}
  .values .v1{font-size:70px;color:var(--yellow)}
  .values .v2{font-size:54px;color:var(--white);margin-top:6px}
  .school-mark{position:absolute;left:600px;top:930px;width:200px;display:flex;flex-direction:column;align-items:center;gap:14px}
  .school-mark .dot{width:110px;height:110px;border-radius:50%;background:var(--yellow)}
  .school-mark .name{font-size:30px;color:var(--yellow);text-align:center;line-height:1.1}
</style>
</head>
<body>
<main class="poster">
  <div class="artwork-bg" role="img" aria-label="First Nations dot artwork pattern in deep greens"></div>

  <h1 class="headline">
    <div class="l1">Are you</div>
    <div class="l2">Ready for</div>
    <div class="l3">Class?</div>
  </h1>

  <div class="emblem-art" role="img" aria-label="Circular dot-painting compass emblem in green and yellow"></div>

  <div class="badge">
    <div class="badge-top"><span class="the">THE</span><span class="name">WENDALE</span></div>
    <div class="badge-nums">
      <span class="n">1</span><span class="comma">,</span>
      <span class="n">2</span><span class="comma">,</span>
      <span class="n">3</span>
    </div>
  </div>

  <section class="steps">
    <div class="step" style="top:380px;height:152px"></div>
    <div class="step-num" style="left:67px;top:415px">1</div>
    <div class="step-icon" style="left:199px;top:391px">
      <svg width="88" height="64" viewBox="0 0 88 64" aria-hidden="true">
        <rect x="12" y="4" width="64" height="44" rx="4" fill="#0b2a17"/>
        <rect x="17" y="9" width="54" height="34" fill="#fff"/>
        <path d="M2 52h84l-5 8H7z" fill="#0b2a17"/>
        <rect x="36" y="52" width="16" height="3" fill="#fff"/>
      </svg>
    </div>
    <div class="step-label" style="top:405px">Laptop /<br>Workbook</div>

    <div class="step" style="top:544px;height:144px"></div>
    <div class="step-num" style="left:67px;top:571px">2</div>
    <div class="step-icon" style="left:199px;top:551px">
      <svg width="70" height="106" viewBox="0 0 70 106" aria-hidden="true">
        <path d="M8 30a27 27 0 0 1 54 0v72H8z" fill="#0b2a17" stroke="#fff" stroke-width="2"/>
        <circle cx="35" cy="20" r="6" fill="none" stroke="#fff" stroke-width="2.5"/>
        <text x="35" y="90" fill="#fff" font-family="Archivo Black, sans-serif" font-size="8" text-anchor="middle">LOCKPOUCH</text>
      </svg>
    </div>
    <div class="step-label" style="top:590px">Phone in Lockpouch</div>

    <div class="step" style="top:696px;height:140px"></div>
    <div class="step-num" style="left:67px;top:721px">3</div>
    <div class="step-icon" style="left:199px;top:701px">
      <svg width="100" height="70" viewBox="0 0 100 70" aria-hidden="true">
        <path d="M24 10h52l6 36H18z" fill="#0b2a17"/>
        <ellipse cx="50" cy="50" rx="48" ry="14" fill="#0b2a17"/>
        <circle cx="40" cy="26" r="3" fill="none" stroke="#fff" stroke-width="1.5"/>
        <circle cx="60" cy="26" r="3" fill="none" stroke="#fff" stroke-width="1.5"/>
      </svg>
    </div>
    <div class="step-label small" style="top:722px">Correct Uniform<br>(Including Hat)</div>
  </section>

  <div class="waves" role="img" aria-label="White dotted flowing river-line artwork"></div>

  <div class="values">
    <div class="v1">Curiosity &amp; Drive</div>
    <div class="v2">Wendale Learner Values</div>
  </div>

  <div class="school-mark">
    <span class="dot"></span>
    <span class="name">WENDALE<br>STATE HIGH</span>
  </div>
</main>
</body>
</html>
```